Business Card Design

I would like a new business card for my business Drive Haven, we operate within the automotive industry and offer customer retention solutions for independent mechanical workshops across Australia and New Zealand. The program incorporates service reminders and roadside assistance for consumers and is designed to get the client back for their vehicle service visit, I would like a doubled sided design that incorporates my logos and a two tone type card that has white and a carbon fibre look also use the blue in the logo I have uploaded. It would be great to have icons as the phone/fax/email etc details for the card are below. The finished design must be a print ready file useable.It would be great if the design could communicate the what type of business we are
Marcus Trelby
General Manager
Drive Haven Pty Ltd
Unit 5/42 Corrin Street
Wexmoor Newcastle NSW 2391
Ph:+61240173500
fax:+61240173600
Mobile:0415889214
Email:info@drivehaven-example.com.au
Updates
I have just upload a carbon fibre background for the business card hope it helps
Hello guys I am sorry fr no feedback I have been away over seas I will send feedback when I return monday
Industry/Entity Type
Automotive
Look and feel

```html
<!DOCTYPE html>
<html lang="en">
<head>
<meta charset="utf-8">
<title>Drive Haven — Business Card</title>
<link href="https://fonts.googleapis.com/css2?family=Open+Sans:wght@400;600;700&display=swap" rel="stylesheet">
<style>
  :root{
    --bg:#e4e4e4;
    --blue:#3cb8f2;
    --panel-grey:#d2d3d5;
    --panel-light:#f1f2f2;
    --black:#050505;
    --ink:#2b2b2b;
    --rule:#9a9a9a;
    --white:#ffffff;
  }
  *{box-sizing:border-box;margin:0;padding:0}
  html,body{width:1200px;height:1173px;overflow:hidden;background:var(--bg);font-family:"Open Sans",sans-serif;color:var(--ink)}
  .sheet{position:relative;width:1200px;height:1173px}
  .card{position:absolute;top:196px;width:460px;height:780px;background:var(--blue);box-shadow:0 2px 6px rgba(0,0,0,.18)}
  .card--front{left:100px}
  .card--back{left:640px}

  /* front */
  .front-url{position:absolute;left:22px;top:22px;right:22px;height:118px;background:var(--panel-grey);border-radius:0 44px 0 0;display:flex;align-items:center;justify-content:center;font-size:21px;letter-spacing:.5px;color:var(--ink)}
  .front-field{position:absolute;left:22px;top:140px;right:22px;bottom:22px;background:var(--black);border-radius:0 0 0 90px;display:flex;align-items:center;justify-content:center}
  .brand{display:flex;align-items:center;gap:14px}
  .brand-dot{width:46px;height:46px;border-radius:50%;background:var(--blue)}
  .brand-name{font-size:34px;font-weight:600;color:var(--white);letter-spacing:.5px}

  /* back */
  .back-panel{position:absolute;left:22px;top:22px;right:22px;bottom:22px;background:var(--panel-grey);border-radius:52px;overflow:hidden}
  .back-top{height:150px;display:flex;align-items:center;justify-content:center}
  .badge{width:100px;height:100px;border-radius:50%;background:var(--blue);border:4px solid var(--white);box-shadow:0 0 0 2px var(--blue)}
  .contact-list{background:var(--panel-light);height:420px;padding:26px 40px 0 50px;list-style:none}
  .contact-item{display:flex;align-items:center;gap:26px;height:92px}
  .contact-icon{flex:0 0 46px;width:46px;height:46px}
  .contact-text{flex:1;font-size:19px;line-height:1.3;padding-bottom:6px;border-bottom:2px solid var(--rule);padding-top:10px}
  .contact-text--plain{border-bottom:2px solid var(--rule)}
  .back-name{text-align:center;padding-top:38px}
  .person{font-size:31px;font-weight:700;letter-spacing:1px;color:#333}
  .role{font-size:27px;color:#333;margin-top:2px}
</style>
</head>
<body>
<div class="sheet">

  <section class="card card--front">
    <div class="front-url">www.drivehaven-example.com</div>
    <div class="front-field">
      <div class="brand">
        <span class="brand-dot"></span>
        <span class="brand-name">Drive Haven</span>
      </div>
    </div>
  </section>

  <section class="card card--back">
    <div class="back-panel">
      <div class="back-top"><div class="badge" aria-hidden="true"></div></div>
      <ul class="contact-list">
        <li class="contact-item">
          <svg class="contact-icon" viewBox="0 0 46 46" aria-hidden="true"><circle cx="23" cy="23" r="20" fill="none" stroke="#222" stroke-width="3"/><path d="M16 13c2-1 4 0 5 3l-2 3c1 3 4 6 7 7l3-2c3 1 4 3 3 5-1 2-3 3-5 3-8-1-14-7-15-15 0-2 1-3 4-4z" fill="none" stroke="#222" stroke-width="2.5"/></svg>
          <span class="contact-text">+98 600 410 27</span>
        </li>
        <li class="contact-item">
          <svg class="contact-icon" viewBox="0 0 46 46" aria-hidden="true"><circle cx="23" cy="23" r="21" fill="#222"/><rect x="12" y="15" width="22" height="16" fill="#fff"/><path d="M12 15l11 9 11-9" fill="none" stroke="#222" stroke-width="2"/></svg>
          <span class="contact-text">mail@drivehaven-example.com</span>
        </li>
        <li class="contact-item">
          <svg class="contact-icon" viewBox="0 0 46 46" aria-hidden="true"><circle cx="23" cy="23" r="20" fill="none" stroke="#222" stroke-width="3"/><circle cx="23" cy="23" r="12" fill="none" stroke="#222" stroke-width="2"/><ellipse cx="23" cy="23" rx="5" ry="12" fill="none" stroke="#222" stroke-width="2"/><path d="M11 23h24M13 17h20M13 29h20" stroke="#222" stroke-width="2"/></svg>
          <span class="contact-text">www.drivehaven-example.com</span>
        </li>
        <li class="contact-item">
          <svg class="contact-icon" viewBox="0 0 46 46" aria-hidden="true"><circle cx="23" cy="23" r="21" fill="#222"/><path d="M23 34s-8-9-8-15a8 8 0 0 1 16 0c0 6-8 15-8 15z" fill="#fff"/><circle cx="23" cy="19" r="3" fill="#222"/></svg>
          <span class="contact-text">Unit 9, Kelso Row, T4R 2B8<br>318 8th Avenue NE</span>
        </li>
      </ul>
      <div class="back-name">
        <div class="person">JONAH STELL</div>
        <div class="role">Founder</div>
      </div>
    </div>
  </section>

</div>
</body>
</html>
```